DLM Homepage Banner

I would like a banner that uses/interprets the existing graphic on the www.janetholmcounsel.example homepage.

Target Market(s)

Business professionals across a variety of industries and sectors.

Requirements
Must have
• Must incorporate all the words and relationships of the existing image (file attached). I am seeking a professional and clean interpretation of the image.
• Must consider the look and feel of the banner on the following page: http://www.janetholmcounsel.example/pathways-in-nordic-crm/ (file attached)
• Must include the DLM logo in a similar style to the banner on the Pathways in Nordic CRM page (file attached).
Nice to have
• Feel free to add background/foreground graphics.
• I like the design idea of "bio-mechanical" applied to a professional services/business industry.
• The overall image must display a "business-technology-people-change" balance.
Should not have
• Should not be a direct replication of the existing graphic but must contain all the words and relationships.

```html
<!DOCTYPE html>
<html lang="en">
<head>
<meta charset="utf-8">
<title>DLM Janet Holm Counsel – Technology Risk Management</title>
<link href="https://fonts.googleapis.com/css2?family=Open+Sans:wght@300;400;600&family=Roboto+Condensed:wght@400;700&display=swap" rel="stylesheet">
<style>
  :root {
    --brand-blue: #1f5aa6;
    --navy: #0e3a73;
    --panel: #f1f1f1;
    --wheel-yellow: #eec900;
    --hub-ring: #c9a800;
    --rim-grey: #a9a9a9;
    --ink: #2a2a2a;
    --ink-soft: #444444;
    --white: #ffffff;
  }
  * { box-sizing: border-box; margin: 0; padding: 0; }
  html, body { width: 1200px; height: 836px; overflow: hidden; background: var(--white); }
  .banner { position: relative; width: 1200px; height: 836px; font-family: "Open Sans", Arial, sans-serif; }

  .brand {
    position: absolute; top: 70px; left: 0; width: 1200px; text-align: center;
    font-family: "Open Sans", Arial, sans-serif; font-weight: 600; font-size: 40px;
    letter-spacing: 2px; color: var(--brand-blue);
  }
  .tagline {
    position: absolute; top: 143px; left: 0; width: 1186px; text-align: center;
    font-weight: 300; font-size: 17.5px; color: var(--ink-soft);
  }
  .panel { position: absolute; left: 47px; top: 203px; width: 1093px; height: 533px; background: var(--panel); }

  .risk { position: absolute; text-align: center; transform: translateX(-50%); white-space: nowrap; }
  .risk-title { font-family: "Roboto Condensed", Arial Narrow, sans-serif; font-weight: 700; font-size: 24px; color: var(--ink); line-height: 1.2; }
  .risk-sub { font-weight: 300; font-size: 17.5px; color: var(--ink-soft); line-height: 1.5; }
  .risk--procure { left: 298px; top: 249px; }
  .risk--independence { left: 582px; top: 214px; }
  .risk--business { left: 850px; top: 254px; }

  .diagram { position: absolute; left: 0; top: 0; }
  .wheel-label { font-family: "Roboto Condensed", Arial Narrow, sans-serif; font-weight: 700; font-size: 23px; fill: var(--ink); text-anchor: middle; dominant-baseline: middle; }
  .wheel-label--small { font-size: 17px; }
  .chevron-label { font-family: "Open Sans", Arial, sans-serif; font-size: 16px; fill: var(--white); text-anchor: middle; dominant-baseline: middle; }
  .chevron-label--small { font-size: 14px; }

  .domains { position: absolute; left: 471px; top: 374px; width: 200px; list-style: none; }
  .domain {
    height: 45px; margin-bottom: 7.5px; background: var(--navy);
    box-shadow: 1px 2px 2px rgba(0,0,0,.25);
    display: flex; align-items: center; justify-content: center;
    font-family: "Roboto Condensed", Arial Narrow, sans-serif; font-weight: 700; font-size: 21px;
    color: var(--white); text-shadow: 1px 1px 1px rgba(0,0,0,.5);
  }
</style>
</head>
<body>
<main class="banner">
  <div class="brand">DLM Janet Holm Counsel</div>
  <p class="tagline">DLM Supports Organisational Technology Risk Management Outcomes</p>

  <section class="panel" aria-hidden="true"></section>

  <div class="risk risk--procure"><div class="risk-title">Procure risk</div><div class="risk-sub">The Right Partner</div></div>
  <div class="risk risk--independence"><div class="risk-title">Independence risk</div><div class="risk-sub">The Right Technology Frames</div></div>
  <div class="risk risk--business"><div class="risk-title">Business risk</div><div class="risk-sub">The Right Outcome</div></div>

  <svg class="diagram" width="1200" height="836" viewBox="0 0 1200 836">
    <!-- independence arrow -->
    <g class="independence-arrow" stroke="var(--ink)" stroke-width="1.5" fill="none">
      <line x1="427" y1="278" x2="739" y2="278"/>
      <polyline points="435,272 427,278 435,284"/>
      <polyline points="731,272 739,278 731,284"/>
    </g>

    <!-- procure wheel -->
    <g class="wheel wheel--procure">
      <circle cx="291" cy="497" r="181" fill="var(--wheel-yellow)" stroke="var(--rim-grey)" stroke-width="5"/>
      <g stroke="var(--white)" stroke-width="7">
        <line x1="291" y1="497" x2="291" y2="319"/>
        <line x1="291" y1="497" x2="460" y2="442"/>
        <line x1="291" y1="497" x2="396" y2="641"/>
        <line x1="291" y1="497" x2="186" y2="641"/>
        <line x1="291" y1="497" x2="122" y2="442"/>
      </g>
      <circle cx="291" cy="497" r="44" fill="var(--hub-ring)"/>
      <circle cx="291" cy="497" r="37" fill="var(--navy)"/>
      <rect x="406" y="652" width="8" height="8" fill="var(--white)" transform="rotate(45 410 656)"/>
      <text class="wheel-label" x="226" y="410">Upgrade</text>
      <text class="wheel-label" x="369" y="410">Evaluate</text>
      <text class="wheel-label" x="182" y="521">Maintain</text>
      <text class="wheel-label" x="403" y="521">Procure</text>
      <text class="wheel-label" x="292" y="624">Implement</text>
    </g>

    <!-- business wheel -->
    <g class="wheel wheel--business">
      <circle cx="849" cy="497" r="181" fill="var(--wheel-yellow)" stroke="var(--rim-grey)" stroke-width="5"/>
      <g stroke="var(--white)" stroke-width="7">
        <line x1="849" y1="497" x2="849" y2="319"/>
        <line x1="849" y1="497" x2="1018" y2="442"/>
        <line x1="849" y1="497" x2="954" y2="641"/>
        <line x1="849" y1="497" x2="744" y2="641"/>
        <line x1="849" y1="497" x2="680" y2="442"/>
      </g>
      <circle cx="849" cy="497" r="44" fill="var(--hub-ring)"/>
      <circle cx="849" cy="497" r="37" fill="var(--navy)"/>
      <rect x="964" y="652" width="8" height="8" fill="var(--white)" transform="rotate(45 968 656)"/>
      <text class="wheel-label" x="789" y="411">Govern</text>
      <text class="wheel-label" x="922" y="417">Change</text>
      <text class="wheel-label wheel-label--small" x="958" y="515">Communication</text>
      <text class="wheel-label" x="749" y="523">Implement</text>
      <text class="wheel-label" x="856" y="617">Process</text>
    </g>

    <!-- people chevrons -->
    <g class="people" fill="var(--navy)">
      <polygon points="446,641 566,641 576,652.5 566,664 446,664 456,652.5"/>
      <polygon points="576,641 696,641 706,652.5 696,664 576,664 586,652.5"/>
      <polygon points="446,667 696,667 706,678.5 696,690 446,690"/>
    </g>
    <text class="chevron-label" x="511" y="653">Analysts</text>
    <text class="chevron-label" x="639" y="653">Advisors</text>
    <text class="chevron-label chevron-label--small" x="574" y="679">Programme Managers</text>
  </svg>

  <ul class="domains">
    <li class="domain">Enterprise Strategy</li>
    <li class="domain">Enterprise Software</li>
    <li class="domain">Enterprise Hardware</li>
    <li class="domain">Enterprise Networks</li>
    <li class="domain">Enterprise Services</li>
  </ul>
</main>
</body>
</html>
```